New Business Card Design for a Payroll Concierge Company

I need a new business card design that is simple and includes my current information. I am a payroll concierge company that processes payroll for clients who employ household employees and I also manage my client's personal bills, financial records. I want to include my current logo and a logo for an association (BFKTR) I belong too on the front of my business card. I will include both my all my company logo files and the association logo files.

Target Market(s)

People who hire household employees, nannies, home health aides, butlers, maids, etc for wealthy individuals and senior citizens who need help in the home.

Industry/Entity Type

Financial Service

Contact Information for Business Card

Company logo

Name: Martin L. Westerby
Managing Director

Office number: 555-472-0183
Business Cell: 555-617-2904

Website: www.brightwagedesk.example
Email: Martin.Westerby@brightwagedesk.example

Company address:

18 Hollin Lane
Suite 427
Linwick,EX 04512

Font styles to use
Serif
Sans Serif

Colors
3176b5
85cae6
cee9f5
33a6d7
d3d3d3
dbdbdb

Requirements
Must have
• I need to have my company logo and name, phone numbers, website, email, and address on the card. I also want the association logo on the card somewhere but not too big. Small enough to see the logo maybe on the top or bottom corner. Or some where on there card that it doesn't take away the design.
Nice to have
• i like the blue color in my logo, grey, please see must haves business card details.
Should not have
• PLEASE DO NOT USE THE BUSINESS CARD DESIGNS IN THE FILES I UPLOADED. I AM NOT INTERESTED IN THAT DESIGN. ALSO THE ADDRESS AND WEBSITE ARE INCORRECT ON THOSE DESIGNS. PLEASE USE THE UPDATED INFO ON BUSINESS CARD DETAILS

```html
<!DOCTYPE html>
<html lang="en">
<head>
<meta charset="utf-8">
<title>Bright Wage Desk – Business Card</title>
<link rel="stylesheet" href="https://fonts.googleapis.com/css2?family=Oswald:wght@600&family=Open+Sans:wght@400;600;700&display=swap">
<style>
  :root {
    --page-bg: #2a2b2d;
    --card-bg: #1f2022;
    --card-edge: #2c2d30;
    --text-light: #e9eaeb;
    --text-muted: #c9cacc;
    --brand-grey: #a9acb0;
    --brand-blue: #3176b5;
    --divider: #8d8f93;
  }
  * { box-sizing: border-box; margin: 0; padding: 0; }
  html, body {
    width: 1200px;
    height: 1000px;
    overflow: hidden;
    background: var(--page-bg);
    font-family: "Open Sans", Arial, sans-serif;
  }
  .canvas {
    position: relative;
    width: 1200px;
    height: 1000px;
  }
  .card {
    position: absolute;
    left: 220px;
    width: 760px;
    height: 430px;
    background: var(--card-bg);
    border: 1px solid var(--card-edge);
    box-shadow: 0 14px 30px rgba(0,0,0,.45);
  }
  .card--front { top: 50px; }
  .card--back  { top: 520px; }

  /* Front */
  .brand {
    position: absolute;
    inset: 0;
    display: flex;
    align-items: center;
    justify-content: center;
    gap: 18px;
  }
  .brand__mark {
    width: 26px;
    height: 26px;
    background: var(--brand-grey);
  }
  .brand__name {
    font-family: "Open Sans", Arial, sans-serif;
    font-weight: 700;
    font-size: 44px;
    letter-spacing: 3px;
    color: var(--brand-grey);
  }

  /* Back */
  .identity {
    position: absolute;
    right: 430px;
    top: 152px;
    text-align: right;
  }
  .identity__name {
    font-family: "Oswald", "Arial Narrow", sans-serif;
    font-weight: 600;
    font-size: 32px;
    line-height: 1.15;
    color: var(--text-light);
    letter-spacing: .5px;
  }
  .identity__title {
    font-size: 22px;
    color: var(--brand-blue);
    letter-spacing: .5px;
    line-height: 1.2;
  }
  .divider {
    position: absolute;
    left: 346px;
    top: 140px;
    width: 2px;
    height: 110px;
    background: var(--divider);
  }
  .contacts {
    position: absolute;
    left: 368px;
    top: 146px;
    list-style: none;
  }
  .contacts__item {
    display: flex;
    align-items: center;
    gap: 12px;
    height: 24px;
    font-size: 16px;
    color: var(--text-muted);
  }
  .contacts__icon {
    width: 16px;
    height: 16px;
    flex: none;
  }
  .contacts__accent { color: var(--brand-blue); }
  .address {
    position: absolute;
    left: 170px;
    top: 345px;
    display: flex;
    align-items: center;
    gap: 12px;
    font-size: 17px;
    color: var(--text-muted);
    letter-spacing: .5px;
  }
  .address__icon { width: 16px; height: 20px; }
  .member-badge {
    position: absolute;
    right: 40px;
    bottom: 34px;
    width: 96px;
    height: 32px;
    background: var(--brand-blue);
    border-radius: 3px;
  }
</style>
</head>
<body>
<main class="canvas">

  <section class="card card--front" aria-label="Card front">
    <div class="brand">
      <span class="brand__mark" aria-hidden="true"></span>
      <span class="brand__name">BRIGHT WAGE DESK</span>
    </div>
  </section>

  <section class="card card--back" aria-label="Card back">
    <div class="identity">
      <h1 class="identity__name">MARTIN L. WESTERBY</h1>
      <p class="identity__title">Managing Director</p>
    </div>

    <span class="divider" aria-hidden="true"></span>

    <ul class="contacts">
      <li class="contacts__item">
        <svg class="contacts__icon" viewBox="0 0 16 16" aria-hidden="true"><path fill="#3176b5" d="M3.5 1.5l2.5 0.3 1 3.2-1.6 1.3c.8 1.7 2.2 3.1 3.9 3.9l1.3-1.6 3.2 1 .3 2.5c0 .8-.6 1.4-1.4 1.4C6.8 13.5 2.5 9.2 2.1 2.9c0-.8.6-1.4 1.4-1.4z"/></svg>
        <span>555 472 0183</span>
      </li>
      <li class="contacts__item">
        <svg class="contacts__icon" viewBox="0 0 16 16" aria-hidden="true"><rect x="4" y="1" width="8" height="14" rx="1.5" fill="none" stroke="#3176b5" stroke-width="1.6"/><circle cx="8" cy="12.5" r=".9" fill="#3176b5"/></svg>
        <span>555 617 2904</span>
      </li>
      <li class="contacts__item">
        <svg class="contacts__icon" viewBox="0 0 16 16" aria-hidden="true"><rect x="1" y="3" width="14" height="10" fill="#3176b5"/><path d="M1 3.5l7 5 7-5" fill="none" stroke="#1f2022" stroke-width="1.3"/></svg>
        <span>martin.westerby@brightwagedesk.example</span>
      </li>
      <li class="contacts__item">
        <svg class="contacts__icon" viewBox="0 0 16 16" aria-hidden="true"><circle cx="8" cy="8" r="7" fill="#3176b5"/><path d="M1 8h14M8 1c-3 3.5-3 10.5 0 14M8 1c3 3.5 3 10.5 0 14" fill="none" stroke="#1f2022" stroke-width="1"/></svg>
        <span>www.<span class="contacts__accent">brightwagedesk</span>.example</span>
      </li>
    </ul>

    <p class="address">
      <svg class="address__icon" viewBox="0 0 16 20" aria-hidden="true"><path fill="#3176b5" d="M8 0a7 7 0 0 0-7 7c0 5 7 13 7 13s7-8 7-13a7 7 0 0 0-7-7zm0 10a3 3 0 1 1 0-6 3 3 0 0 1 0 6z"/></svg>
      <span>18 Hollin Lane Suite 427 Linwick,EX 04512</span>
    </p>

    <span class="member-badge" role="img" aria-label="BFKTR association membership badge"></span>
  </section>

</main>
</body>
</html>
```